Business Card and Simple Logo Desgin

New Zealand based start up company "Brava Advisory LTD" requires business cards and simple logo design.

Card Content.

Brava Advisory LTD

Rosalind Kettering
CA, BMS (Hons)

r.kettering@bravaadvisory.example.nz
PH +64 21 705 146

Target Market(s)

Corporate Business in IT, Finance and accounting.

Industry/Entity Type

Business

```html
<!DOCTYPE html>
<html lang="en">
<head>
<meta charset="utf-8">
<title>Brava Advisory LTD – Business Card</title>
<link rel="stylesheet" href="https://fonts.googleapis.com/css2?family=Source+Sans+3:wght@400;600;700&display=swap">
<style>
  :root {
    --card-bg: #000000;
    --card-edge: #8a8a8a;
    --text-main: #ffffff;
    --accent-green: #6cbf0c;
    --accent-orange: #ff6a00;
    --accent-blue: #0a3cff;
    --page-bg: #ffffff;
  }
  * { margin: 0; padding: 0; box-sizing: border-box; }
  html, body {
    width: 1200px;
    height: 695px;
    overflow: hidden;
    background: var(--page-bg);
  }
  .business-card {
    position: relative;
    width: 1200px;
    height: 695px;
    background: var(--card-bg);
    border: 2px solid var(--card-edge);
    font-family: "Source Sans 3", "Myriad Pro", Arial, sans-serif;
    color: var(--text-main);
    overflow: hidden;
  }
  .brand {
    position: absolute;
    left: 92px;
    top: 92px;
    display: flex;
    align-items: center;
    gap: 34px;
  }
  .brand-dot {
    width: 150px;
    height: 150px;
    flex: none;
  }
  .brand-name {
    font-size: 54px;
    font-weight: 700;
    letter-spacing: -0.5px;
    color: var(--text-main);
    white-space: nowrap;
  }
  .contact {
    position: absolute;
    left: 90px;
    top: 342px;
    font-size: 30px;
    line-height: 1;
  }
  .contact-name {
    font-weight: 700;
    font-size: 30px;
  }
  .contact-credentials {
    margin-top: 33px;
    font-weight: 400;
  }
  .contact-email {
    margin-top: 80px;
    font-weight: 400;
  }
  .contact-phone {
    margin-top: 33px;
    font-weight: 400;
  }
  .colour-strip {
    position: absolute;
    top: 0;
    right: 52px;
    width: 24px;
    height: 100%;
    display: flex;
    flex-direction: column;
  }
  .colour-strip span { display: block; flex: 1; }
  .strip-green { background: var(--accent-green); }
  .strip-orange { background: var(--accent-orange); }
  .strip-blue { background: var(--accent-blue); }
</style>
</head>
<body>
  <main class="business-card">
    <header class="brand">
      <svg class="brand-dot" viewBox="0 0 150 150" aria-hidden="true">
        <circle cx="75" cy="75" r="66" fill="var(--accent-orange)"/>
      </svg>
      <h1 class="brand-name">Brava Advisory LTD</h1>
    </header>

    <section class="contact">
      <p class="contact-name">Rosalind Kettering</p>
      <p class="contact-credentials">CA, BMS (Hons)</p>
      <p class="contact-email">r.kettering@bravaadvisory.example.nz</p>
      <p class="contact-phone">PH +64 21 705 146</p>
    </section>

    <div class="colour-strip" aria-hidden="true">
      <span class="strip-green"></span>
      <span class="strip-orange"></span>
      <span class="strip-blue"></span>
    </div>
  </main>
</body>
</html>
```